Wedding invitation

Hello,

I would like the same attached image in a vertical rectangular 3D effect design, same colours,
but without text.

I would like eaxctly like the attachment design, in a long vertical, ration 16:9 size for social media.

```html
<!DOCTYPE html>
<html lang="en">
<head>
<meta charset="utf-8">
<title>Wedding Invitation Frame</title>
<style>
  :root {
    --page-bg: #ffffff;
    --card-bg: #ffffff;
    --navy: #2b3140;
    --navy-soft: #3a4050;
    --gold-light: #d9ad72;
    --gold: #b9874e;
    --gold-deep: #8e6333;
    --shade: rgba(20, 24, 34, 0.28);
  }
  html, body {
    margin: 0;
    padding: 0;
    width: 878px;
    height: 1200px;
    overflow: hidden;
    background: var(--page-bg);
  }
  .invitation {
    position: relative;
    width: 878px;
    height: 1200px;
  }
  .invitation-frame {
    display: block;
    width: 878px;
    height: 1200px;
  }
</style>
</head>
<body>
  <main class="invitation">
    <svg class="invitation-frame" viewBox="0 0 878 1200" xmlns="http://www.w3.org/2000/svg" aria-hidden="true">
      <defs>
        <linearGradient id="gold-stroke" x1="0" y1="0" x2="1" y2="1">
          <stop offset="0" stop-color="#d9ad72"/>
          <stop offset="0.5" stop-color="#b9874e"/>
          <stop offset="1" stop-color="#8e6333"/>
        </linearGradient>
        <linearGradient id="card-sheen" x1="0" y1="0" x2="0" y2="1">
          <stop offset="0" stop-color="#f1eeea"/>
          <stop offset="0.15" stop-color="#ffffff"/>
          <stop offset="1" stop-color="#ffffff"/>
        </linearGradient>
        <filter id="card-shadow" x="-10%" y="-10%" width="120%" height="120%">
          <feDropShadow dx="0" dy="3" stdDeviation="5" flood-color="rgba(20,24,34,0.28)"/>
        </filter>
      </defs>

      <!-- 9:16 card, centred on the canvas -->
      <rect class="card-border" x="124" y="40" width="630" height="1120"
            fill="#ffffff" stroke="#2b3140" stroke-width="14" filter="url(#card-shadow)"/>

      <!-- soft sheen at the top inside the gold frame -->
      <rect class="card-sheen" x="171" y="108" width="518" height="180" fill="url(#card-sheen)"/>

      <!-- thin navy rule, shifted up and right -->
      <rect class="navy-rule" x="179" y="75" width="538" height="1057"
            fill="none" stroke="#3a4050" stroke-width="3"/>

      <!-- gold double frame, shifted down and left -->
      <rect class="gold-frame-outer" x="161" y="98" width="538" height="1012"
            fill="none" stroke="url(#gold-stroke)" stroke-width="5"/>
      <rect class="gold-frame-inner" x="171" y="108" width="518" height="992"
            fill="none" stroke="url(#gold-stroke)" stroke-width="3"/>
    </svg>
  </main>
</body>
</html>
```